Brochure for solar, battery back up and generators

I want to create some brochure type print media, it can be something we print in house.

I want it to show options with some detail for various products from Marvix to Quenby Amberdock.

What I am imagining is a few graphical depictions, of the final product, some detail in capability and some blanks for load calcs, very simple not a real load calc, and a place for a price.

```html
<!DOCTYPE html>
<html lang="en">
<head>
<meta charset="utf-8">
<title>Solvane Power Tri-fold Brochure</title>
<link href="https://fonts.googleapis.com/css2?family=Oswald:wght@500;600&family=Roboto:wght@400;500;700;900&display=swap" rel="stylesheet">
<style>
:root{
  --green:#2f9e3f;
  --green-dark:#1f7d2e;
  --orange:#ee6a1e;
  --orange-head:#e5561a;
  --yellow:#f7d417;
  --text:#2e2e2e;
  --muted:#6b6b6b;
  --white:#ffffff;
  --canvas:#676a6e;
}
*{margin:0;padding:0;box-sizing:border-box}
html,body{width:1200px;height:2734px;overflow:hidden}
body{background:var(--canvas);font-family:"Roboto",sans-serif;color:var(--text);position:relative}
.spread{position:absolute;left:50px;width:1100px;height:850px;overflow:hidden;background:var(--white);box-shadow:0 10px 30px rgba(0,0,0,.35)}
.spread--outside{top:470px}
.spread--inside{top:1410px}
.spread-art{position:absolute;inset:0;width:1100px;height:850px}
.block{position:absolute}
p{font-size:13px;line-height:16px}
.h-green{font-weight:700;color:var(--green);font-size:24px;text-decoration:underline;text-decoration-thickness:2px;text-underline-offset:3px}
.h-orange{font-weight:700;color:var(--orange-head);font-size:18px;line-height:22px}
.about{left:38px;top:34px;width:290px}
.about .h-orange{margin:4px 0 6px}
.about p{margin-bottom:14px}
.about h3.h-orange{margin-top:6px}
.brand{font-family:"Roboto",sans-serif;font-weight:900;font-size:30px;letter-spacing:-.5px;display:flex;align-items:center;gap:8px}
.brand-dot{width:22px;height:22px;border-radius:50%;background:var(--yellow);flex:none}
.brand-tag{font-size:10px;font-weight:500;margin-top:2px}
.cover-brand{left:733px;width:367px;top:56px;display:flex;flex-direction:column;align-items:center}
.cover-brand .brand{color:var(--green)}
.cover-brand .brand-tag{color:var(--orange)}
.cover-headline{left:733px;width:367px;top:646px;text-align:center;font-family:"Oswald",sans-serif;font-weight:600;font-size:26px;line-height:33px;color:var(--white)}
.cover-headline .accent{color:var(--yellow)}
.web-pill{left:800px;top:790px;width:234px;height:34px;border-radius:17px;background:var(--yellow);color:#1d3d12;font-weight:700;font-size:16px;display:flex;align-items:center;justify-content:center}
.contact{left:405px;top:622px;width:330px;color:var(--white)}
.contact .brand{color:var(--white);font-size:28px}
.contact .brand-tag{color:var(--white)}
.contact h4{color:var(--yellow);font-weight:700;font-size:17px;letter-spacing:.5px;margin:14px 0 8px}
.contact ul{list-style:none}
.contact li{display:flex;align-items:flex-start;gap:8px;font-size:15px;line-height:20px;margin-bottom:2px}
.contact-icon{width:16px;height:16px;border-radius:50%;background:var(--yellow);flex:none;margin-top:2px;display:flex;align-items:center;justify-content:center}
.why{left:38px;top:38px;width:310px;color:var(--white)}
.why h2{font-size:19px;font-weight:700;color:var(--yellow);text-decoration:underline;text-underline-offset:3px;margin-bottom:6px}
.why > p{font-size:13px;line-height:16.5px}
.feature{position:absolute;left:38px;width:300px;display:flex;gap:18px;color:var(--white)}
.icon-box{width:62px;height:62px;border-radius:6px;display:flex;align-items:center;justify-content:center;flex:none}
.icon-box--orange{background:var(--orange)}
.icon-box--green{background:var(--green)}
.icon-box--amber{background:#f3a21b}
.feature h3{font-size:15px;font-weight:500;letter-spacing:.2px}
.feature p{font-size:12.5px;line-height:15px}
.inside-brand{left:38px;top:560px;color:var(--white)}
.inside-brand .brand{color:var(--white);font-size:28px}
.trust{left:408px;top:36px;width:290px}
.trust p{font-size:12.5px;line-height:15.5px}
.trust p,.roofing p{text-align:justify}
.trust .h-orange,.roofing .h-orange{margin-bottom:6px}
.service{position:absolute;left:408px;width:290px;display:flex;gap:18px}
.service .icon-box{width:54px;height:54px}
.service h3{font-size:13.5px;font-weight:700;text-transform:uppercase}
.service p{font-size:11.5px;line-height:13.5px}
.spec-fields{display:flex;gap:8px;margin-top:3px;font-size:10.5px;font-weight:700;color:var(--green-dark)}
.spec-fields span{white-space:nowrap}
.blank{display:inline-block;border-bottom:1px solid var(--muted);height:10px;vertical-align:baseline;margin-left:2px}
.side-service{position:absolute;left:772px;width:300px;display:flex;gap:16px}
.side-service .icon-box{width:56px;height:56px}
.side-service h3{font-size:14px;font-weight:700;text-transform:uppercase}
.side-service p{font-size:12.5px;line-height:15px}
.roofing{left:772px;top:456px;width:288px}
.roofing p{font-size:12.5px;line-height:15.5px}
</style>
</head>
<body>

<section class="spread spread--outside">
  <svg class="spread-art" viewBox="0 0 1100 850">
    <defs>
      <linearGradient id="handFade" x1="0" y1="0" x2="0" y2="1">
        <stop offset="0" stop-color="#ffffff"/>
        <stop offset=".3" stop-color="#f3c98a"/>
        <stop offset=".7" stop-color="#c98752"/>
        <stop offset="1" stop-color="#3c4a66"/>
      </linearGradient>
      <linearGradient id="roofPhoto" x1="0" y1="0" x2="0" y2="1">
        <stop offset="0" stop-color="#8fb7c8"/>
        <stop offset=".3" stop-color="#6f9552"/>
        <stop offset=".6" stop-color="#4b5a70"/>
        <stop offset="1" stop-color="#2c3650"/>
      </linearGradient>
      <linearGradient id="greenTint" x1="0" y1="0" x2="1" y2="1">
        <stop offset="0" stop-color="#3cae48"/>
        <stop offset="1" stop-color="#27903a"/>
      </linearGradient>
      <radialGradient id="aerial" cx=".5" cy=".5" r=".6">
        <stop offset="0" stop-color="#c9c9c4"/>
        <stop offset="1" stop-color="#5f7f4c"/>
      </radialGradient>
    </defs>
    <rect x="0" y="500" width="366" height="350" fill="url(#handFade)" role="img" aria-label="Photo of a hand resting on a solar panel at sunset"/>
    <rect x="366" y="0" width="734" height="850" fill="url(#roofPhoto)" role="img" aria-label="Photo of two installers in hard hats fitting solar panels on a roof above vineyards"/>
    <rect x="733" y="0" width="367" height="124" fill="#ffffff"/>
    <path d="M366 0 L545 0 C470 200 440 400 470 600 L366 640 Z" fill="url(#greenTint)" role="img" aria-label="Green-toned photo of a house roof"/>
    <circle cx="519" cy="400" r="112" fill="none" stroke="var(--yellow)" stroke-width="3"/>
    <circle cx="519" cy="400" r="100" fill="url(#aerial)" stroke="#ffffff" stroke-width="5" role="img" aria-label="Aerial photo of a home with solar panels"/>
    <path d="M690 850 L690 712 C735 628 850 586 1100 590 L1100 850 Z" fill="var(--green)"/>
    <path d="M690 712 C735 628 850 586 1100 590" fill="none" stroke="var(--yellow)" stroke-width="3" transform="translate(0,-8)"/>
    <path d="M366 850 L366 660 C400 590 460 556 540 556 C640 556 720 610 750 700 C765 745 772 800 772 850 Z" fill="var(--orange)"/>
    <path d="M366 648 C400 578 460 542 540 542 C645 542 728 598 760 692 C776 740 784 800 784 850" fill="none" stroke="var(--yellow)" stroke-width="3"/>
  </svg>

  <div class="block about">
    <h2 class="h-green">About Us</h2>
    <h3 class="h-orange">Provide Power Security and Independence With Self Generation and Backup Power Solutions</h3>
    <p>Solvane Power's mission is to provide Energy Independence through direct Engineering, designed by in house Electrical Engineer(s) and technical staff to effectively safeguard against soaring power cost increases and power outages.</p>
    <p>Our team's passion for advanced technologies in power generation and Uninterruptible Power has proven to be incredibly successful!</p>
    <h3 class="h-orange">Environmental Dedication From the Start</h3>
    <p>Solvane Power was founded over 20 years ago as an engineering &amp; disaster relief organization working with state and federal entities. As word spread and the quality of our services gained a reputation throughout California, we began to receive requests from personal residences. We soon honed in on our environmental responsibilities and chose to dedicate our expertise to this cause. Thousands of residential solar power projects later, we are honored to continue making a positive impact on the world. If you're ready to work with our passionate, knowledgeable team of contractors, give us a call today to get started.</p>
  </div>

  <div class="block contact">
    <div class="brand">Solvane Power<span class="brand-dot"></span></div>
    <div class="brand-tag">Solvane Environmental &amp; Construction Services</div>
    <h4>CONTACT US</h4>
    <ul>
      <li><span class="contact-icon"><svg width="10" height="10" viewBox="0 0 10 10"><path d="M5 1a3 3 0 0 1 3 3c0 2-3 5-3 5S2 6 2 4a3 3 0 0 1 3-3z" fill="#ee6a1e"/></svg></span><span>218 Larkspur Ridge Rd #140<br>Fairmont, CA 95012</span></li>
      <li><span class="contact-icon"><svg width="10" height="10" viewBox="0 0 10 10"><path d="M2 1l2 2-1 1.2a6 6 0 0 0 2.8 2.8L7 6l2 2-1.2 1.2C4.5 9 1 5.5.8 2.2z" fill="#ee6a1e"/></svg></span><span>555-014-2270</span></li>
      <li><span class="contact-icon"><svg width="10" height="10" viewBox="0 0 10 10"><rect x="1" y="2.5" width="8" height="5.5" fill="#ee6a1e"/><path d="M1 2.5l4 3 4-3" stroke="#f7d417" fill="none"/></svg></span><span>info@solvanepower.com</span></li>
      <li><span class="contact-icon"><svg width="10" height="10" viewBox="0 0 10 10"><circle cx="5" cy="5" r="3.6" fill="none" stroke="#ee6a1e" stroke-width="1.2"/><path d="M1.4 5h7.2M5 1.4v7.2" stroke="#ee6a1e"/></svg></span><span>www.solvanepower.com</span></li>
    </ul>
  </div>

  <div class="block cover-brand">
    <div class="brand">Solvane Power<span class="brand-dot"></span></div>
    <div class="brand-tag">Solvane Environmental &amp; Construction Services</div>
  </div>

  <h1 class="block cover-headline">A REVOLUTIONARY SOLUTION<br><span class="accent">FOR THE RISING COST OF</span><br>ENERGY &amp; POWER OUTAGES</h1>
  <div class="block web-pill">www.solvanepower.com</div>
</section>

<section class="spread spread--inside">
  <svg class="spread-art" viewBox="0 0 1100 850">
    <defs>
      <linearGradient id="workerPhoto" x1="0" y1="0" x2="1" y2="1">
        <stop offset="0" stop-color="#8a7a6e"/>
        <stop offset=".5" stop-color="#3e4f86"/>
        <stop offset="1" stop-color="#2a3a78"/>
      </linearGradient>
      <linearGradient id="treesFade" x1="0" y1="0" x2="0" y2="1">
        <stop offset="0" stop-color="#ffffff"/>
        <stop offset=".45" stop-color="#b9cbd6"/>
        <stop offset="1" stop-color="#5c8a45"/>
      </linearGradient>
      <linearGradient id="aerialRoof" x1="0" y1="0" x2="1" y2="1">
        <stop offset="0" stop-color="#9aa3ad"/>
        <stop offset=".5" stop-color="#2e3f78"/>
        <stop offset="1" stop-color="#5d8a4a"/>
      </linearGradient>
    </defs>
    <path d="M0 0 L405 0 C372 200 360 420 398 560 C418 640 402 700 382 770 L0 770 Z" fill="var(--green)"/>
    <path d="M405 0 C372 200 360 420 398 560 C418 640 402 700 382 770" fill="none" stroke="var(--yellow)" stroke-width="3" transform="translate(8,0)"/>
    <rect x="700" y="740" width="400" height="110" fill="url(#treesFade)" role="img" aria-label="Photo of treetops under a blue sky"/>
    <path d="M0 640 C130 600 280 630 430 720 L440 850 L0 850 Z" fill="url(#workerPhoto)" role="img" aria-label="Photo of an installer working on rooftop solar panels"/>
    <rect x="772" y="232" width="286" height="188" fill="url(#aerialRoof)" role="img" aria-label="Aerial photo of a house with solar panels and a pool"/>
  </svg>

  <div class="block why">
    <h2>WHY CHOOSE US</h2>
    <p>Our focus has always been on science – not sales. We believe in the quality of our products and are confident that you'll be satisfied with every aspect of your experience. The team of contractors at Solvane Power provides exceptional customer service while designing, installing, and maintaining our wide range of products.</p>
  </div>

  <div class="feature" style="top:212px">
    <div class="icon-box icon-box--amber"><svg width="38" height="38" viewBox="0 0 38 38" fill="none" stroke="#fff" stroke-width="2" stroke-linejoin="round"><path d="M3 14l8-4 8 5 8-5 8 4M7 20l8 8c2 2 4 2 6 0l8-8M13 18l6 6M17 16l6 6"/></svg></div>
    <div><h3>CUSTOMER FOCUS</h3><p>We are proud to offer financing options for every homeowner &amp; property owner, regardless of credit score.</p></div>
  </div>
  <div class="feature" style="top:318px">
    <div class="icon-box icon-box--orange"><svg width="38" height="38" viewBox="0 0 38 38" fill="none" stroke="#fff" stroke-width="2"><circle cx="19" cy="16" r="9"/><path d="M15 27h8M16 31h6M19 12v6"/></svg></div>
    <div><h3>NO OBLIGATIONS</h3><p>When you book an obligation-free assessment, you'll immediately receive a free quote for our services without any visits from salespeople.</p></div>
  </div>
  <div class="feature" style="top:432px">
    <div class="icon-box icon-box--amber"><svg width="38" height="38" viewBox="0 0 38 38" fill="none" stroke="#fff" stroke-width="2"><circle cx="19" cy="15" r="10"/><path d="M14 15l4 4 6-7M13 24l-3 10 5-3 4 3M25 24l3 10-5-3"/></svg></div>
    <div><h3>TOP QUALITY</h3><p>You can count on us to provide you with the best products in the solar power industry at fixed, affordable prices.</p></div>
  </div>

  <div class="block inside-brand">
    <div class="brand">Solvane Power<span class="brand-dot"></span></div>
    <div class="brand-tag">Solvane Environmental &amp; Construction Services</div>
  </div>

  <div class="block trust">
    <h2 class="h-orange">Environmental and Construction Services You Can Trust</h2>
    <p>Although we specialize in solar energy design and installation, you can count on us for all of your home or business power system needs. Our dedication to the environment comes to life through every job we complete – whether we are fitting your home with sustainable roofing materials, installing electric vehicle chargers, or transforming your home's source of energy. No matter what type of construction project you have in mind, the quality and efficiency of our work will exceed your expectations. Give us a call today to make the switch to a clean, safe energy alternative with a knowledgeable team.</p>
  </div>

  <div class="service" style="top:314px">
    <div class="icon-box icon-box--orange"><svg width="32" height="32" viewBox="0 0 34 34" fill="none" stroke="#fff" stroke-width="2" stroke-linejoin="round"><path d="M4 17L17 6l13 11M8 14v14h18V14"/><path d="M13 20h8v8h-8z"/></svg></div>
    <div><h3>Solar</h3><p>We are transforming the world of energy through comprehensive solar power system design, installation, &amp; maintenance services.</p>
      <div class="spec-fields"><span>Load<span class="blank" style="width:34px"></span> kW</span><span>Price $<span class="blank" style="width:50px"></span></span></div></div>
  </div>
  <div class="service" style="top:410px">
    <div class="icon-box icon-box--green"><svg width="32" height="32" viewBox="0 0 34 34" fill="none" stroke="#fff" stroke-width="2"><rect x="10" y="7" width="14" height="22" rx="2"/><path d="M14 4h6"/><path d="M18 12l-3 6h4l-3 6" stroke-linejoin="round"/></svg></div>
    <div><h3>Battery Backup</h3><p>Options from Marvix to Quenby Amberdock give you confidence in your home's source of energy.</p>
      <div class="spec-fields"><span>Load<span class="blank" style="width:34px"></span> kWh</span><span>Price $<span class="blank" style="width:50px"></span></span></div></div>
  </div>
  <div class="service" style="top:494px">
    <div class="icon-box icon-box--orange"><svg width="32" height="32" viewBox="0 0 34 34" fill="none" stroke="#fff" stroke-width="2"><path d="M7 17a10 10 0 0 1 17-7M27 17a10 10 0 0 1-17 7"/><path d="M24 4v6h-6M10 30v-6h6"/><path d="M18 12l-3 5h4l-3 5"/></svg></div>
    <div><h3>Generators</h3><p>We provide solar-powered generators that will ease your worries during the next power outage in your California neighborhood.</p>
      <div class="spec-fields"><span>Load<span class="blank" style="width:34px"></span> kW</span><span>Price $<span class="blank" style="width:50px"></span></span></div></div>
  </div>
  <div class="service" style="top:592px">
    <div class="icon-box icon-box--green"><svg width="32" height="32" viewBox="0 0 34 34" fill="none" stroke="#fff" stroke-width="2" stroke-linejoin="round"><path d="M6 22v-5l3-7h16l3 7v5z"/><path d="M8 22v4h4v-4M22 22v4h4v-4M6 17h22"/><circle cx="11" cy="19.5" r="1"/><circle cx="23" cy="19.5" r="1"/></svg></div>
    <div><h3>EV Charger</h3><p>Our high-power electric vehicle (EV) chargers are paving the way for a cleaner future. We provide professional recommendations and home installation services.</p>
      <div class="spec-fields"><span>Load<span class="blank" style="width:34px"></span> kW</span><span>Price $<span class="blank" style="width:50px"></span></span></div></div>
  </div>

  <div class="side-service" style="top:42px">
    <div class="icon-box icon-box--green"><svg width="34" height="34" viewBox="0 0 34 34" fill="none" stroke="#fff" stroke-width="2" stroke-linejoin="round"><rect x="7" y="6" width="13" height="22" rx="1"/><path d="M5 28h17M20 12h4v10a2 2 0 0 0 4 0V10l-3-3"/><path d="M14 11l-3 5h4l-3 5"/></svg></div>
    <div><h3>EV Stations Commercial</h3><p>Our team can help design and install top-quality EV charging stations for your commercial building or multi-family residence.</p></div>
  </div>
  <div class="side-service" style="top:134px">
    <div class="icon-box icon-box--orange"><svg width="34" height="34" viewBox="0 0 34 34" fill="none" stroke="#fff" stroke-width="2"><path d="M8 6h18l2 4v14l-2 4H8l-2-4V10z"/><path d="M13 12v4M21 12v4M17 19l-2 4h4l-2 4"/></svg></div>
    <div><h3>Electrical Contractors</h3><p>We are equipped with decades of electrical experience &amp; are ready to handle your repair, replacement, upgrade, &amp; emergency needs.</p></div>
  </div>

  <div class="block roofing">
    <h2 class="h-orange">Roofing Services From a Team of Experts</h2>
    <p>Although we specialize in solar energy design and installation, you can count on us for all of your home or business power system needs. Our dedication to the environment comes to life through every job we complete – whether we are fitting your home with sustainable roofing materials, installing electric vehicle chargers, or transforming your home's source of energy. No matter what type of construction project you have in mind, the quality and efficiency of our work will exceed your expectations. Give us a call today to make the switch to a clean, safe energy alternative with a knowledgeable team.</p>
  </div>
</section>

</body>
</html>
```